Recycling Depot Business Card Design

We need a double sided business card for our recycling depot business. Please include name, position, address, phone, cell, fax, email and website address. Business card should match the colour scheme of our logo and look environmental but modern. I've attached a few business cards from Mintvale Works that I like.

Industry/Entity Type

Recycling

Contact Information for Business Card

Please include name, position, address, phone, cell, fax, email and website address.

Font styles to use
Sans Serif

Requirements
Must have
• Our Logo, Colour Scheme that matches our logo. Use of Colour Gradients and a custom look.

```html
<!DOCTYPE html>
<html lang="en">
<head>
<meta charset="utf-8">
<title>Cyclora – Business Card</title>
<link href="https://fonts.googleapis.com/css2?family=Montserrat:wght@400;500;700&display=swap" rel="stylesheet">
<style>
  :root {
    --backdrop: #2b2b2b;
    --lime: #9ccd3c;
    --leaf: #4fae45;
    --forest: #1f6a36;
    --pale-ring: rgba(255,255,255,0.22);
    --white: #ffffff;
    --brand-green: #1f6a36;
  }
  html, body {
    margin: 0;
    padding: 0;
    overflow: hidden;
  }
  body {
    width: 1200px;
    height: 528px;
    background: var(--backdrop);
    font-family: "Montserrat", Arial, sans-serif;
  }
  .card-sheet {
    position: relative;
    width: 1200px;
    height: 528px;
    display: flex;
    justify-content: center;
    align-items: center;
    gap: 40px;
  }
  .card {
    width: 540px;
    height: 309px;
    border-radius: 12px;
    overflow: hidden;
    box-shadow: 0 14px 28px rgba(0,0,0,0.45);
    display: block;
  }
  .brand-name {
    font-family: "Montserrat", Arial, sans-serif;
    font-weight: 700;
    fill: var(--brand-green);
  }
  .holder-name {
    font-weight: 500;
    fill: var(--white);
    font-size: 30px;
  }
  .holder-role {
    font-weight: 500;
    fill: var(--white);
    font-size: 14px;
  }
  .contact-line {
    font-weight: 400;
    fill: var(--white);
    font-size: 12px;
  }
  .contact-icon {
    fill: none;
    stroke: var(--white);
    stroke-width: 1.2;
  }
  .contact-glyph {
    fill: var(--white);
  }
</style>
</head>
<body>
<main class="card-sheet">

  <!-- Front side -->
  <svg class="card card-front" viewBox="0 0 540 309" xmlns="http://www.w3.org/2000/svg" aria-label="Front of card">
    <defs>
      <linearGradient id="front-field" x1="0" y1="0" x2="1" y2="0.3">
        <stop offset="0" stop-color="var(--lime)"/>
        <stop offset="0.38" stop-color="var(--leaf)"/>
        <stop offset="0.58" stop-color="var(--forest)"/>
        <stop offset="1" stop-color="var(--forest)"/>
      </linearGradient>
    </defs>
    <rect width="540" height="309" fill="url(#front-field)"/>
    <circle cx="269" cy="153" r="226" fill="var(--pale-ring)"/>
    <circle cx="269" cy="153" r="214" fill="var(--pale-ring)"/>
    <circle cx="269" cy="153" r="202" fill="var(--white)"/>
    <circle cx="154" cy="152" r="22" fill="var(--leaf)"/>
    <text class="brand-name" x="186" y="167" font-size="42">Cyclora</text>
  </svg>

  <!-- Back side -->
  <svg class="card card-back" viewBox="0 0 540 309" xmlns="http://www.w3.org/2000/svg" aria-label="Back of card">
    <rect width="540" height="309" fill="var(--white)"/>
    <circle cx="-300" cy="155" r="630" fill="var(--lime)"/>
    <circle cx="-300" cy="155" r="617" fill="var(--leaf)"/>
    <circle cx="-300" cy="155" r="604" fill="var(--forest)"/>

    <circle cx="316" cy="154" r="42" fill="var(--white)"/>
    <circle cx="316" cy="154" r="18" fill="var(--leaf)"/>
    <text class="brand-name" x="366" y="166" font-size="34">Cyclora</text>

    <text class="holder-name" x="46" y="78">Name Here</text>
    <text class="holder-role" x="46" y="100">Position Here</text>

    <g class="contact-list">
      <g transform="translate(0,161)">
        <circle class="contact-icon" cx="52" cy="0" r="7"/>
        <path class="contact-glyph" d="M49 -3 l2 -1 1 2 -1 1 q1 2 3 3 l1 -1 2 1 -1 2 q-5 0 -7 -7z"/>
        <text class="contact-line" x="66" y="4">Office: 555-201-4470</text>
      </g>
      <g transform="translate(0,186)">
        <circle class="contact-icon" cx="52" cy="0" r="7"/>
        <path class="contact-glyph" d="M49 -3 l2 -1 1 2 -1 1 q1 2 3 3 l1 -1 2 1 -1 2 q-5 0 -7 -7z"/>
        <text class="contact-line" x="66" y="4">Mobile: 555-201-4471</text>
      </g>
      <g transform="translate(0,211)">
        <circle class="contact-icon" cx="52" cy="0" r="7"/>
        <rect class="contact-icon" x="48.5" y="-2.5" width="7" height="5" stroke-width="1"/>
        <text class="contact-line" x="66" y="4">Fax: 555-201-4472</text>
      </g>
      <g transform="translate(0,236)">
        <circle class="contact-icon" cx="52" cy="0" r="7"/>
        <circle class="contact-icon" cx="52" cy="0" r="3.5" stroke-width="1"/>
        <line class="contact-icon" x1="48.5" y1="0" x2="55.5" y2="0" stroke-width="1"/>
        <text class="contact-line" x="66" y="4">www.cyclora.com</text>
      </g>
      <g transform="translate(0,261)">
        <circle class="contact-icon" cx="52" cy="0" r="7"/>
        <rect class="contact-icon" x="48.5" y="-2.5" width="7" height="5" stroke-width="1"/>
        <path class="contact-icon" d="M48.5 -2.5 L52 0.5 L55.5 -2.5" stroke-width="1"/>
        <text class="contact-line" x="66" y="4">info@cyclora.com</text>
      </g>
    </g>
  </svg>

</main>
</body>
</html>
```